Website Design for WeselneKarety.pl – Luxury Wedding Car Rental with Chauffeur

We are looking for a talented designer to create a modern, elegant, and fully responsive website for our new brand – WeselnyKarety.pl. We are a premium car rental platform in Poland, offering luxury and exotic vehicles exclusively for weddings. All cars come with a professional chauffeur, ensuring a high-end, stress-free, and stylish experience.
Website Purpose:
The website should present our offering in a luxurious, clear, and inspiring way. It must build trust, highlight the prestige of our brand, and encourage inquiries. Our target audience includes engaged couples, wedding planners, and clients seeking a truly exceptional vehicle for their special day.
Design Requirements:
Style: modern, elegant, minimalist
Color palette: white, black, gold, optionally silver – refined and luxurious
Typography: clean, modern, high-end
Layout: clear, intuitive, with large car images and well-defined sections
Fully responsive (desktop, tablet, mobile)
Bilingual layout (Polish/English) must be considered
Pages to Design:
Homepage
About Us
Fleet Overview
Individual Car Pages
Services (Weddings, Photo Shoots, Film Rentals)
Why Us / Unique Selling Points
Contact
FAQ
Inspiration:
Luxury automotive brands (e.g. Varnell-Dorne, Corwick, Elsby Havard)
High-end wedding websites
Minimalist layouts with large visuals and elegant typography
Additional Notes:
The design should evoke the emotions of a wedding day – elegance, uniqueness, style, and class. Please avoid flashy colors, excessive graphic effects, or overly decorative elements. Subtlety, prestige, and sophistication are key.

```html
<!DOCTYPE html>
<html lang="en">
<head>
<meta charset="utf-8">
<title>WeselneKarety.pl – Premium Car Rental</title>
<link href="https://fonts.googleapis.com/css2?family=Syncopate:wght@700&family=Lato:wght@400;700&display=swap" rel="stylesheet">
<style>
:root{
  --navy:#1c2b42;
  --navy-dark:#142033;
  --navy-card:#22334d;
  --gold:#e3bd55;
  --white:#ffffff;
  --muted:#b9c2d0;
  --line:#3a4a63;
}
*{margin:0;padding:0;box-sizing:border-box}
html,body{width:1200px;height:4573px;overflow:hidden}
body{position:relative;background:var(--navy);font-family:'Lato',sans-serif;color:var(--white)}
.abs{position:absolute}
.display{font-family:'Syncopate',sans-serif;font-weight:700;letter-spacing:4px;text-transform:uppercase;white-space:nowrap}
.section-title{font-size:36px;color:var(--gold);letter-spacing:6px}
.btn{position:absolute;display:flex;align-items:center;justify-content:center;gap:6px;height:26px;border-radius:13px;font-size:9px;font-weight:700;letter-spacing:.6px;text-transform:uppercase;white-space:nowrap}
.btn-gold{background:var(--gold);color:#1a1a1a}
.btn-outline{border:1.5px solid var(--gold);color:var(--white)}
.photo{position:absolute;overflow:hidden}

/* hero */
.hero{position:absolute;left:0;top:0;width:1200px;height:628px;background:#1d1d20}
.hero-shade{position:absolute;inset:0;background:linear-gradient(90deg,rgba(10,12,16,.55) 0%,rgba(10,12,16,.1) 60%,rgba(10,12,16,.3) 100%)}
.brand{position:absolute;left:70px;top:26px;display:flex;align-items:center;gap:8px;font-size:18px;font-weight:700;color:var(--gold)}
.brand i{display:block;width:10px;height:10px;border-radius:50%;background:var(--gold)}
.nav a{position:absolute;top:34px;font-size:9.5px;font-weight:700;color:var(--white);text-decoration:none;text-transform:uppercase;letter-spacing:.4px;white-space:nowrap}
.nav a.active{color:var(--gold);border-bottom:1.5px solid var(--gold);padding-bottom:3px}
.hero-title{left:192px;top:268px;font-size:42px;letter-spacing:5px;color:var(--white)}
.hero-title span{color:var(--gold)}
.hero-sub{left:192px;top:332px;font-size:17px;line-height:23px;color:var(--white)}
.dot{position:absolute;left:1053px;width:13px;height:13px;border-radius:50%;border:1.5px solid var(--white)}
.dot.on::after{content:"";position:absolute;left:3px;top:3px;width:4px;height:4px;border-radius:50%;background:var(--white)}

/* featured */
.featured{position:absolute;left:0;top:628px;width:1200px;height:509px;background:var(--navy)}
.lead{font-size:11px;line-height:17px;color:var(--white)}
.car-card{position:absolute;top:122px;height:258px;border-radius:10px;overflow:hidden}
.car-card .name{position:absolute;left:18px;bottom:38px;font-size:15px;font-weight:700;white-space:nowrap}
.car-card .price{position:absolute;left:18px;bottom:18px;font-size:10px;font-weight:700;white-space:nowrap}
.car-card.faded{opacity:.5}
.round{position:absolute;width:28px;height:28px;border-radius:50%;display:flex;align-items:center;justify-content:center}

/* services */
.services{position:absolute;left:0;top:1137px;width:1200px;height:433px;background:var(--navy-dark)}
.service-card{position:absolute;top:124px;width:263px;height:244px;border-radius:10px;background:var(--navy-card)}
.service-card h3{position:absolute;left:24px;top:106px;font-size:12.5px;font-weight:700}
.service-card p{position:absolute;left:24px;top:130px;width:200px;font-size:9.5px;line-height:14px;font-weight:700;color:#dfe4ec}
.service-card .icon{position:absolute;left:24px;top:46px}
.service-card .go{left:24px;top:181px;border:1.5px solid var(--muted)}

/* about */
.about-text{left:670px;top:1776px;width:338px;font-size:11.5px;line-height:17.5px;color:#dfe4ec}
.about-text p+p{margin-top:17px}

/* gallery */
.tile{position:absolute;border-radius:9px;overflow:hidden}

/* cta */
.cta{position:absolute;left:192px;top:3300px;width:816px;height:244px;border-radius:12px;background:linear-gradient(180deg,#2a2f38 0%,#1a1d24 100%);overflow:hidden}
.cta h2{position:absolute;left:0;top:42px;width:816px;text-align:center;font-size:27px;line-height:38px;letter-spacing:4px;color:var(--gold)}
.cta h2 span{color:var(--white)}

/* faq */
.faq-row{position:absolute;left:298px;width:604px;height:50px;border-bottom:1px solid var(--line);display:flex;align-items:center}
.faq-row .num{width:28px;height:28px;border-radius:50%;border:1.5px solid var(--muted);display:flex;align-items:center;justify-content:center;font-size:11px;margin-right:22px}
.faq-row .q{font-size:11px;font-weight:700;flex:1}
.faq-row .plus{font-size:20px;color:var(--muted);margin-right:6px}
.faq-open{position:absolute;left:298px;top:3741px;width:604px;height:222px;background:#1f3150;border-bottom:1px solid var(--line)}
.faq-open .answer{position:absolute;left:18px;top:66px;width:560px;font-size:11px;line-height:17px;color:#dfe4ec}
.faq-open .answer p+p{margin-top:17px}

/* footer */
.footer{position:absolute;left:0;top:4161px;width:1200px;height:412px;background:radial-gradient(ellipse at 50% 20%,#2a2522 0%,#15161a 55%,#0d0e11 100%)}
.f-label{font-size:9px;font-weight:700;letter-spacing:3px;text-transform:uppercase}
.f-value{font-size:13px;color:var(--gold);letter-spacing:2px;white-space:nowrap}
.f-head{position:absolute;font-size:12px;color:var(--gold);letter-spacing:3px}
.f-list{position:absolute;list-style:none;font-size:9px;font-weight:700;text-transform:uppercase;line-height:16.5px}
.f-list li:first-child{color:var(--gold)}
.field{position:absolute;width:190px;border-bottom:1px solid #5a5f68;font-size:9.5px;font-weight:700;padding-bottom:6px}
.social{position:absolute;width:26px;height:26px;border-radius:50%;border:1.5px solid var(--gold)}
</style>
</head>
<body>

<!-- HERO -->
<header class="hero">
  <div class="photo" role="img" aria-label="Black luxury limousine parked in front of a stately stone building at dusk" style="inset:0;background:radial-gradient(ellipse at 62% 55%,#3a3a3e 0%,#1b1b1f 45%,transparent 70%),linear-gradient(180deg,#4a3f30 0%,#2a2520 55%,#1d1c1d 100%)"></div>
  <div class="hero-shade"></div>
  <div class="brand"><i></i>WeselneKarety</div>
  <nav class="nav">
    <a class="active" style="left:295px">Home</a>
    <a style="left:351px">About Us</a>
    <a style="left:428px">Fleet Overview</a>
    <a style="left:543px">Individual Car</a>
    <a style="left:654px">Services</a>
    <a style="left:729px">Why Us</a>
    <a style="left:795px">FAQ</a>
    <a style="left:838px">Contact</a>
    <a style="left:942px">ENG ▾</a>
  </nav>
  <div class="btn btn-outline" style="left:1003px;top:27px;width:128px">Reserve now →</div>
  <h1 class="abs display hero-title">Premium Car <span>Rental</span></h1>
  <p class="abs hero-sub">Extensive Fleet of Premium Cars.<br>Best Rental Terms.</p>
  <div class="btn btn-gold" style="left:192px;top:403px;width:128px">Reserve now →</div>
  <div class="btn btn-outline" style="left:338px;top:403px;width:124px">Inquiry now! →</div>
  <span class="dot" style="top:328px"></span>
  <span class="dot on" style="top:347px"></span>
  <span class="dot" style="top:366px"></span>
</header>

<!-- FEATURED CARS -->
<section class="featured">
  <h2 class="abs display section-title" style="left:192px;top:62px">Featured Cars</h2>
  <p class="abs lead" style="left:633px;top:68px;width:380px">Lorem Ipsum is simply dummy text of the printing and typesetting industry. Lorem Ipsum has been the industry's standard dummy text ever since.</p>

  <div class="car-card faded" style="left:0;width:178px">
    <div class="photo" role="img" aria-label="Sports car on an open road under a dark sky" style="inset:0;background:linear-gradient(180deg,#4b5360 0%,#2a2f37 100%)"></div>
  </div>
  <div class="car-card" style="left:192px;width:401px">
    <div class="photo" role="img" aria-label="Black Varnell-Dorne saloon parked beside modern steps" style="inset:0;background:linear-gradient(180deg,#8b8f94 0%,#3d3f43 55%,#17181a 100%)"></div>
    <div class="name">Varnell-Dorne - Sovereign</div>
    <div class="price">From 300 zł/day</div>
  </div>
  <div class="car-card" style="left:607px;width:401px">
    <div class="photo" role="img" aria-label="Blue Corwick grand tourer in front of a city building" style="inset:0;background:linear-gradient(180deg,#b59572 0%,#24508e 50%,#122a4d 100%)"></div>
    <div class="name">Corwick - Meridian GT</div>
    <div class="price">From 300 zł/day</div>
  </div>
  <div class="car-card faded" style="left:1022px;width:178px">
    <div class="photo" role="img" aria-label="Grey Elsby Havard coupe on a village street" style="inset:0;background:linear-gradient(180deg,#6d6a66 0%,#3b3d40 100%)"></div>
    <div class="name">Elsby Havard - Solstice</div>
    <div class="price">From 340 zł/day</div>
  </div>

  <div class="btn btn-outline" style="left:192px;top:409px;width:134px">Show all cars →</div>
  <div class="round" style="left:935px;top:408px;border:1.5px solid var(--muted)">
    <svg width="10" height="10" viewBox="0 0 10 10"><path d="M8 5H2M4.5 2.5 2 5l2.5 2.5" stroke="#fff" stroke-width="1.3" fill="none"/></svg>
  </div>
  <div class="round" style="left:975px;top:408px;background:var(--gold)">
    <svg width="10" height="10" viewBox="0 0 10 10"><path d="M2 5h6M5.5 2.5 8 5 5.5 7.5" stroke="#1a1a1a" stroke-width="1.3" fill="none"/></svg>
  </div>
</section>

<!-- SERVICES -->
<section class="services">
  <h2 class="abs display section-title" style="left:192px;top:76px">Our Services</h2>
  <div class="btn btn-outline" style="left:877px;top:86px;width:131px">Inquiry now! →</div>

  <article class="service-card" style="left:192px">
    <svg class="icon" width="56" height="50" viewBox="0 0 56 50" fill="none" stroke="#e3bd55" stroke-width="2"><circle cx="20" cy="30" r="12"/><circle cx="36" cy="30" r="12"/><path d="M28 4c-3-4-9-1-6 4l6 6 6-6c3-5-3-8-6-4z"/></svg>
    <h3>Car Rental for Weddings</h3>
    <p>Enhance your rental experience with additional options.</p>
    <div class="round go"><svg width="10" height="10" viewBox="0 0 10 10"><path d="M2.5 7.5 7.5 2.5M3.5 2.5h4v4" stroke="#fff" stroke-width="1.3" fill="none"/></svg></div>
  </article>

  <article class="service-card" style="left:469px;overflow:hidden">
    <div class="photo" role="img" aria-label="Wedding couple posing beside a luxury car for a photo shoot" style="inset:0;background:linear-gradient(180deg,#4a5060 0%,#2d3444 100%);opacity:.85"></div>
    <svg class="icon" width="56" height="50" viewBox="0 0 56 50" fill="none" stroke="#e3bd55" stroke-width="2"><rect x="4" y="14" width="46" height="30" rx="4"/><circle cx="27" cy="29" r="9"/><path d="M18 14l4-7h10l4 7"/></svg>
    <h3>Photo Shoots</h3>
    <p>Enhance your rental experience with additional options.</p>
    <div class="round go" style="background:var(--gold);border-color:var(--gold)"><svg width="10" height="10" viewBox="0 0 10 10"><path d="M2.5 7.5 7.5 2.5M3.5 2.5h4v4" stroke="#1a1a1a" stroke-width="1.3" fill="none"/></svg></div>
  </article>

  <article class="service-card" style="left:745px">
    <svg class="icon" width="56" height="50" viewBox="0 0 56 50" fill="none" stroke="#e3bd55" stroke-width="2"><circle cx="24" cy="26" r="18"/><circle cx="24" cy="15" r="4"/><circle cx="24" cy="37" r="4"/><circle cx="13" cy="26" r="4"/><circle cx="35" cy="26" r="4"/><path d="M42 26h10v10"/></svg>
    <h3>Film Rentals</h3>
    <p>Enhance your rental experience with additional options.</p>
    <div class="round go"><svg width="10" height="10" viewBox="0 0 10 10"><path d="M2.5 7.5 7.5 2.5M3.5 2.5h4v4" stroke="#fff" stroke-width="1.3" fill="none"/></svg></div>
  </article>
</section>

<!-- ABOUT -->
<section class="about">
  <div class="photo" role="img" aria-label="Bride and groom embracing beside a black luxury car in an elegant hall" style="left:196px;top:1646px;width:398px;height:398px;border-radius:50%;border:3px solid #fff;background:linear-gradient(180deg,#c7a27a 0%,#7a5a40 50%,#1f1a18 100%)"></div>
  <div class="photo" role="img" aria-label="Groom in a blue suit standing by a black sports car" style="left:399px;top:1904px;width:210px;height:210px;border-radius:50%;border:3px solid #fff;background:linear-gradient(180deg,#3f5b3a 0%,#263427 55%,#17191c 100%)"></div>
  <svg class="abs" style="left:930px;top:1920px" width="130" height="130" viewBox="0 0 130 130"><circle cx="65" cy="65" r="62" fill="none" stroke="#2b3d58" stroke-width="2"/></svg>
  <h2 class="abs display section-title" style="left:635px;top:1722px">About Us</h2>
  <div class="abs about-text">
    <p>It is a long established fact that a reader will be distracted by the readable content of a page when looking at its layout. The point of using Lorem Ipsum is that it has a more-or-less normal distribution of letters, as opposed to using 'Content here, content here', making it look like readable English.</p>
    <p>Many desktop publishing packages and web page editors now use Lorem Ipsum as their default model text, and a search for 'lorem ipsum' will uncover many web sites still in their infancy. Various versions have evolved over the years, sometimes by accident, sometimes on purpose (injected humour and the like).</p>
  </div>
  <div class="btn btn-gold" style="left:670px;top:2007px;width:104px">About us →</div>
  <div class="btn btn-outline" style="left:790px;top:2007px;width:124px">Inquiry now! →</div>
  <div class="abs" style="left:192px;top:2192px;width:816px;height:1px;background:var(--line)"></div>
</section>

<!-- GALLERY -->
<section class="gallery">
  <h2 class="abs display section-title" style="left:0;width:1200px;text-align:center;top:2258px">Photos Gallery</h2>
  <div class="tile" role="img" aria-label="Front view of a black luxury limousine by a classic building" style="left:66px;top:2316px;width:527px;height:525px;background:linear-gradient(180deg,#8c7a5c 0%,#4a4034 45%,#151517 100%)"></div>
  <div class="tile" role="img" aria-label="Black saloon parked in front of concrete steps" style="left:607px;top:2316px;width:256px;height:258px;background:linear-gradient(180deg,#a3a6aa 0%,#4d4f53 60%,#1a1b1d 100%)"></div>
  <div class="tile" role="img" aria-label="Groom standing next to an orange grand tourer at sunset" style="left:874px;top:2316px;width:258px;height:527px;background:linear-gradient(180deg,#caa173 0%,#8a5a32 50%,#2a2624 100%)"></div>
  <div class="tile" role="img" aria-label="Grey sports coupe on a cobbled village street" style="left:607px;top:2588px;width:256px;height:525px;background:linear-gradient(180deg,#59544c 0%,#3e3b37 55%,#222325 100%)"></div>
  <div class="tile" role="img" aria-label="Bride and groom kissing beside a black car indoors" style="left:66px;top:2857px;width:257px;height:256px;background:linear-gradient(180deg,#c8a27c 0%,#6d5441 60%,#1e1a18 100%)"></div>
  <div class="tile" role="img" aria-label="Blue grand tourer front grille close-up" style="left:335px;top:2857px;width:258px;height:256px;background:linear-gradient(180deg,#c9933f 0%,#2a5596 45%,#10284b 100%)"></div>
  <div class="tile" role="img" aria-label="Wedding couple beside a black car in a green garden" style="left:874px;top:2857px;width:258px;height:256px;background:linear-gradient(180deg,#6e8a5b 0%,#3c4d36 55%,#1c1e20 100%)"></div>
</section>

<!-- CTA -->
<section>
  <div class="cta">
    <h2 class="display">Our fleet to hire car starts<br><span>only from $199 per day</span> with<br>aprofessional chauffeur!</h2>
    <div class="btn btn-gold" style="left:324px;top:174px;width:168px">Checkout packages →</div>
  </div>
  <div class="photo" role="img" aria-label="White convertible luxury car" style="left:652px;top:3207px;width:356px;height:122px;border-radius:60px 80px 30px 30px;background:linear-gradient(180deg,#f4f4f4 0%,#c9ccd1 60%,#6c7078 100%)"></div>
</section>

<!-- FAQ -->
<section class="faq">
  <h2 class="abs display section-title" style="left:0;width:1200px;text-align:center;top:3612px">FAQ's</h2>
  <div class="faq-row" style="top:3681px"><span class="num">1.</span><span class="q">What Do I Need To Rent A Car?</span><span class="plus">+</span></div>
  <div class="faq-open">
    <div class="faq-row" style="left:0;top:0;width:604px;border-bottom:none"><span class="num" style="background:var(--gold);border-color:var(--gold);color:#1a1a1a">2.</span><span class="q" style="color:var(--gold)">How Old Do I Need To Be To Rent A Car?</span><span class="plus">−</span></div>
    <div class="abs" style="left:0;top:50px;width:604px;height:1px;background:var(--line)"></div>
    <div class="answer">
      <p>Lorem ipsum dolor sit amet, consectetur adipiscing elit, sed do eiusmod tempor incididunt ut labore et dolore magna aliqua. Quis ipsum suspendisse ultrices gravida. Risus commodo viverra maecenas accumsan lacus vel facilisis.</p>
      <p>Lorem ipsum dolor sit amet, consectetur adipiscing elit, sed do eiusmod tempor incididunt ut labore et dolore magna aliqua. Quis ipsum suspendisse ultrices gravida. Risus commodo viverra maecenas accumsan lacus vel facilisis.</p>
    </div>
  </div>
  <div class="faq-row" style="top:3971px"><span class="num">3.</span><span class="q">Can I Rent A Car With A Debit Card?</span><span class="plus">+</span></div>
  <div class="btn btn-gold" style="left:540px;top:4049px;width:120px">View all FAQ's →</div>
</section>

<!-- FOOTER -->
<footer class="footer"></footer>
<div class="photo" role="img" aria-label="Dimmed night photo of a couple beside a luxury car" style="left:0;top:4161px;width:1200px;height:412px;background:radial-gradient(ellipse at 30% 30%,rgba(90,70,55,.35) 0%,transparent 55%),radial-gradient(ellipse at 85% 40%,rgba(90,70,55,.3) 0%,transparent 50%)"></div>

<svg class="abs" style="left:186px;top:4206px" width="24" height="24" viewBox="0 0 24 24"><path d="M6 3h4l2 5-3 2a11 11 0 0 0 5 5l2-3 5 2v4a2 2 0 0 1-2 2A17 17 0 0 1 4 5a2 2 0 0 1 2-2z" fill="none" stroke="#fff" stroke-width="1.6"/></svg>
<div class="abs" style="left:242px;top:4204px"><div class="f-label">Phone</div><div class="f-value" style="margin-top:4px">+01 555 310 742</div></div>

<div class="abs" style="left:0;width:1200px;top:4207px;display:flex;justify-content:center;align-items:center;gap:8px;font-size:20px;font-weight:700;color:var(--gold)"><span style="display:block;width:10px;height:10px;border-radius:50%;background:var(--gold)"></span>WeselneKarety</div>

<svg class="abs" style="left:752px;top:4206px" width="24" height="24" viewBox="0 0 24 24"><path d="M3 10 12 3l9 7v10H3z M3 10l9 6 9-6" fill="none" stroke="#fff" stroke-width="1.6"/></svg>
<div class="abs" style="left:806px;top:4204px"><div class="f-label">Email</div><div class="f-value" style="margin-top:4px">INFO@WESELNYKARETY.PL</div></div>

<div class="abs" style="left:192px;top:4278px;width:816px;height:1px;background:#3a3b40"></div>

<h3 class="f-head display" style="left:192px;top:4322px">Quick Links</h3>
<ul class="f-list" style="left:192px;top:4358px">
  <li>Home</li><li>About Us</li><li>Fleet Overview</li><li>Individual Car</li><li>Services</li><li>Why Us</li><li>FAQ</li><li>Contact Us</li>
</ul>

<h3 class="f-head display" style="left:398px;top:4322px">Our Services</h3>
<ul class="f-list" style="left:398px;top:4358px">
  <li style="color:#fff">Car Rental for Weddings</li><li>Photo Shoots</li><li>Film Rentals</li>
</ul>
<h3 class="f-head display" style="left:398px;top:4424px">Connect With Us</h3>
<span class="social" style="left:398px;top:4462px"></span>
<span class="social" style="left:434px;top:4462px;background:var(--gold)"></span>
<span class="social" style="left:470px;top:4462px"></span>
<span class="social" style="left:506px;top:4462px"></span>

<h3 class="f-head display" style="left:605px;top:4322px">Inquiry Now!</h3>
<div class="field" style="left:605px;top:4360px">Full Name</div>
<div class="field" style="left:811px;top:4360px">Email Address</div>
<div class="field" style="left:605px;top:4399px">Phone Number</div>
<div class="field" style="left:811px;top:4399px">Select Services <span style="float:right">⌄</span></div>
<div class="field" style="left:605px;top:4438px;width:396px;border-bottom:none">Message...</div>
<div class="abs" style="left:605px;top:4480px;width:365px;height:1px;background:#5a5f68"></div>
<div class="round" style="left:975px;top:4465px;background:var(--gold)"><svg width="10" height="10" viewBox="0 0 10 10"><path d="M2 5h6M5.5 2.5 8 5 5.5 7.5" stroke="#1a1a1a" stroke-width="1.3" fill="none"/></svg></div>

<div class="abs" style="left:192px;top:4524px;width:816px;height:1px;background:#3a3b40"></div>
<p class="abs" style="left:192px;top:4540px;font-size:9px;font-weight:700">Copyright © 2025 <span style="color:var(--gold);text-decoration:underline">Weselne Karety</span>. All Rights Reserved.</p>
<p class="abs" style="left:806px;top:4540px;font-size:9px;font-weight:700">Privacy Policy &nbsp;&nbsp;|&nbsp;&nbsp; Terms and Conditions</p>

</body>
</html>
```